Vacation giveaway landing page design

We are giving away a holiday/vacation to Rome and we need a landing page designed that will entice people to enter their email address for a chance to win!

Full brief, examples and everything else can be found in this document: https://files.brintowle.net/papers/p/4-wxkoppTR7mnbQ2vyLazcR5xsjfPe3lhmwcKt27r/view?mode=linked

1 page

```html
<!DOCTYPE html>
<html lang="en">
<head>
<meta charset="utf-8">
<title>Wanderlot – Win a Holiday to Rome</title>
<link rel="stylesheet" href="https://fonts.googleapis.com/css2?family=Fira+Sans+Extra+Condensed:wght@500;600;700;800&family=Open+Sans:wght@400;600;700&display=swap">
<style>
:root{
  --stage:#5a706e;
  --white:#ffffff;
  --blue:#2b7db4;
  --orange:#f0a500;
  --red:#e8322e;
  --teal:#2db8b1;
  --sky:#38aef0;
  --sand:#f1eee8;
  --ink:#222222;
  --muted:#666666;
  --card:#e9e9e9;
  --gold:#f2c531;
}
*{margin:0;padding:0;box-sizing:border-box}
html,body{width:1200px;height:1200px;overflow:hidden;background:var(--stage)}
body{position:relative;font-family:"Open Sans",sans-serif}
.page{position:absolute;left:436px;top:36px;width:328px;height:1127px;background:var(--white);overflow:hidden}
.head{font-family:"Fira Sans Extra Condensed",sans-serif}
.abs{position:absolute}
.center{left:0;width:100%;text-align:center}

/* hero */
.hero{left:0;top:0;width:328px;height:170px;background:linear-gradient(90deg,#6b4a2c 0%,#b7823e 22%,#f7c257 40%,#f9c65c 60%,#c98e4a 78%,#7a5a3e 100%)}
.brand{left:126px;top:9px;display:flex;align-items:center;gap:4px}
.brand-dot{width:13px;height:13px;border-radius:50%;border:1.5px solid #5b3a1e}
.brand-name{font-family:"Fira Sans Extra Condensed",sans-serif;font-weight:700;font-size:11px;color:#5b3a1e}
.eyebrow{left:113px;top:50px;font-weight:700;font-size:8px;color:#5b2d12}
.prize{left:110px;top:54px;font-weight:800;font-size:45px;line-height:1;color:var(--red);letter-spacing:-.5px}
.nights{left:114px;top:94px;font-weight:700;font-size:11px;color:var(--red)}
.rome-box{left:113px;top:108px;width:94px;height:33px;background:var(--blue);color:var(--white);font-weight:800;font-size:34px;line-height:33px;text-align:center}
.flights{left:113px;top:144px;font-weight:600;font-size:9px;color:var(--white);display:flex;gap:3px;align-items:center}
.stars{color:var(--orange);font-size:8px;letter-spacing:1px}

/* intro */
.avatar{left:134px;top:199px;width:61px;height:61px;border-radius:50%;background:radial-gradient(circle at 50% 60%,#3a6b8a 0 40%,#f7bf3a 41%)}
.tagline{top:267px;font-weight:600;font-size:12px;color:var(--orange)}
.tagline b{color:var(--red);font-weight:700}
.promise{top:283px;font-weight:700;font-size:15px;line-height:17px;color:var(--blue)}

/* countdown */
.countdown{left:0;top:337px;width:328px;height:137px;background:linear-gradient(180deg,#f2efe9 0%,#e8e4dc 60%,#dedad2 100%)}
.hurry{top:352px;font-weight:600;font-size:12px;color:var(--blue)}
.hurry span{color:var(--orange)}
.tile{top:381px;width:39px;height:46px;background:var(--white);border-radius:3px;box-shadow:0 1px 3px rgba(0,0,0,.15);text-align:center}
.tile .num{display:block;font-weight:700;font-size:20px;line-height:24px;margin-top:5px;color:var(--blue)}
.tile .lbl{display:block;font-weight:700;font-size:9px;color:var(--orange)}
.sep{top:399px;font-size:9px;color:#888;font-weight:700}
.btn{height:13px;border-radius:7px;color:var(--white);font-family:"Fira Sans Extra Condensed",sans-serif;font-weight:700;font-size:7px;letter-spacing:.6px;line-height:13px;text-align:center}
.btn-orange{background:var(--orange)}
.btn-red{background:var(--red)}

/* form */
.contact{left:0;top:474px;width:328px;height:165px;background:var(--teal)}
.contact-title{top:498px;font-weight:500;font-size:11px;color:var(--white)}
.field{left:73px;width:181px;height:12px;border-radius:6px;background:var(--white);font-size:4px;font-weight:600;color:var(--teal);line-height:12px;padding-left:6px}

/* winners */
.winners-title{top:661px;font-weight:700;font-size:13px;color:var(--teal)}
.wcard{top:694px;width:60px;height:121px;background:var(--card);border-radius:2px}
.wcard.featured{top:692px;height:128px;background:var(--gold)}
.post{position:absolute;left:4px;top:4px;width:52px;height:88px;background:var(--white)}
.post-head{display:flex;align-items:center;gap:2px;padding:2px}
.post-head i{width:5px;height:5px;background:#ccc;display:block}
.post-head span{font-size:2.6px;font-weight:700;color:var(--ink)}
.post-photo{margin:0 2px;height:40px;background:linear-gradient(160deg,#3b3550,#7a5a78 60%,#2c2a3a)}
.post-text{font-size:2.3px;line-height:3px;color:var(--ink);padding:2px 3px}
.wcap{position:absolute;left:0;width:100%;text-align:center}
.wcap-title{top:98px;font-family:"Fira Sans Extra Condensed",sans-serif;font-weight:600;font-size:5.5px;color:var(--ink)}
.wcap-sub{top:106px;font-size:3px;font-weight:700;line-height:4.5px;color:var(--ink)}
.seal{position:absolute;right:-6px;top:28px;width:16px;height:16px;border-radius:50%;background:#e8b820;border:1.5px solid #c8331f}
.ribbon{position:absolute;left:-6px;top:100px;width:72px;height:8px;background:#d22a26;color:var(--white);font-family:"Fira Sans Extra Condensed",sans-serif;font-weight:600;font-size:5px;line-height:8px;text-align:center}

/* why join */
.why{left:0;top:848px;width:328px;height:279px;background:var(--sky)}
.clouds{left:0;top:848px;width:328px;height:52px;background:linear-gradient(180deg,rgba(255,255,255,.55),rgba(255,255,255,0))}
.why-title{top:871px;font-weight:600;font-size:13px;color:var(--white)}
.perks{top:908px;width:78px;list-style:none}
.perks li{position:relative;padding-left:6px;font-family:"Fira Sans Extra Condensed",sans-serif;font-weight:500;font-size:4.6px;line-height:6px;color:var(--white);margin-bottom:6.5px}
.perks li::before{content:"";position:absolute;left:0;top:2px;width:2px;height:2px;border-radius:50%;background:var(--gold)}
.waiting{top:994px;font-weight:600;font-size:12px;color:var(--white)}
.ruins{left:0;top:1040px;width:328px;height:87px;background:linear-gradient(180deg,rgba(56,174,240,0) 0%,#6ea9c4 45%,#4e8ca6 100%)}
.links{top:1047px;display:flex;justify-content:center;gap:26px;font-family:"Fira Sans Extra Condensed",sans-serif;font-weight:600;font-size:5.2px;letter-spacing:.3px;color:var(--white)}
.legal{top:1076px;font-size:3.6px;line-height:7px;color:var(--white);font-weight:600}
</style>
</head>
<body>
<main class="page">

  <section class="abs hero" role="img" aria-label="Rome photo collage: saint statue, dome and Colosseum with a couple of tourists taking photos"></section>
  <div class="abs brand"><span class="brand-dot"></span><span class="brand-name">Wanderlot</span></div>
  <p class="abs head eyebrow">THIS MONTH'S</p>
  <h1 class="abs head prize">PRIZE</h1>
  <p class="abs head nights">4 NIGHT, 2 PEOPLE</p>
  <p class="abs head rome-box">ROME</p>
  <p class="abs head flights">Flights + Hotel <span class="stars">★★★★</span></p>

  <div class="abs avatar" role="img" aria-label="Cheerful traveller in a floral shirt on a yellow circle"></div>
  <p class="abs center head tagline">Live your <b>Best Live</b></p>
  <h2 class="abs center head promise">YOU'LL NEVER PAY FULL PRICE<br>FOR A HOLIDAY AGAIN</h2>

  <section class="abs countdown" role="img" aria-label="Faded skyline of Rome"></section>
  <p class="abs center head hurry"><span>Hurry!</span> Prize Draw Closes in</p>
  <div class="abs tile head" style="left:63px"><span class="num">03</span><span class="lbl">DAYS</span></div>
  <span class="abs sep" style="left:106px">:</span>
  <div class="abs tile head" style="left:117px"><span class="num">11</span><span class="lbl">HOURS</span></div>
  <span class="abs sep" style="left:161px">:</span>
  <div class="abs tile head" style="left:171px"><span class="num">33</span><span class="lbl">MIN</span></div>
  <span class="abs sep" style="left:215px">:</span>
  <div class="abs tile head" style="left:226px"><span class="num">58</span><span class="lbl">SEC</span></div>
  <div class="abs btn btn-orange" style="left:131px;top:439px;width:66px">JOIN NOW</div>

  <section class="abs contact"></section>
  <p class="abs center head contact-title">Call or Contact US below for details</p>
  <div class="abs field" style="top:522px">Name</div>
  <div class="abs field" style="top:541px">Email</div>
  <div class="abs field" style="top:559px">Phone</div>
  <div class="abs field" style="top:578px">Address</div>
  <div class="abs btn btn-red" style="left:131px;top:601px;width:66px">SEND</div>

  <h2 class="abs center head winners-title">Recent Winners</h2>
  <article class="abs wcard" style="left:64px">
    <div class="post">
      <div class="post-head"><i></i><span>Wanderlot</span></div>
      <div class="post-photo" role="img" aria-label="Winner holding a prize sign"></div>
      <p class="post-text">Maya is our lucky winner this month! She's off to see the Northern Lights.</p>
    </div>
    <p class="wcap wcap-title">JANUARY'S WINNER</p>
    <p class="wcap wcap-sub">This Month Prize:<br>a Northern Lights Gateway</p>
  </article>
  <article class="abs wcard featured" style="left:134px">
    <div class="post">
      <div class="post-head"><i></i><span>Wanderlot</span></div>
      <div class="post-photo" role="img" aria-label="Winner smiling with a prize sign"></div>
      <p class="post-text">Looks like Lena is the lucky one as she's won a trip to Valencia!</p>
    </div>
    <span class="seal"></span>
    <p class="ribbon">DECEMBER'S WINNER</p>
    <p class="wcap wcap-sub" style="top:111px">This Month Prize:<br>a Holiday in Valencia, Spain</p>
  </article>
  <article class="abs wcard" style="left:205px">
    <div class="post">
      <div class="post-head"><i></i><span>Wanderlot</span></div>
      <div class="post-photo" role="img" aria-label="Two winners celebrating together"></div>
      <p class="post-text">Congrats to this month's winner Ruth! She was speechless when we told her.</p>
    </div>
    <p class="wcap wcap-title">NOVEMBER'S WINNER</p>
    <p class="wcap wcap-sub">This Month Prize:<br>a Gateway in Rome, Italy</p>
  </article>

  <section class="abs why"></section>
  <div class="abs clouds" role="img" aria-label="Soft white clouds along the top of the sky"></div>
  <h2 class="abs center head why-title">Why Join?</h2>
  <ul class="abs perks" style="left:46px">
    <li>A chance to win a dream holiday every month</li>
    <li>Unbelievably cheap flight deals long haul &amp; short haul</li>
    <li>Super discounts on hotels, transport, package deals, experiences and more</li>
  </ul>
  <ul class="abs perks" style="left:129px;top:907px">
    <li>Cancel anytime</li>
    <li>Never miss out with convenient automatic renewal</li>
    <li>The more members we have, the better deals we can get you</li>
    <li>Coming soon - exclusive members only discount area</li>
  </ul>
  <ul class="abs perks" style="left:215px;top:907px">
    <li>Monthly awe-inspiring stories and &amp; how to guides in a digital magazine</li>
    <li>Save £400 on most flight deals and up to 90% on hotels and experiences</li>
    <li>Everything direct to your inbox</li>
  </ul>
  <p class="abs center head waiting">So what are you waiting for?</p>
  <div class="abs btn btn-red" style="left:131px;top:1019px;width:66px">JOIN NOW</div>
  <div class="abs ruins" role="img" aria-label="Ancient Roman forum ruins in a blue tint"></div>
  <nav class="abs center links"><span>CONTACT US</span><span>TERMS &amp; CONDITIONS</span><span>PRIVACY POLICY</span></nav>
  <p class="abs center legal">Contact: +44 (0) 200 000 0000 | Email: hello@wanderlotclub.com<br>© 2017 Velmora Ltd a private limited company registered in England and Wales, Reg No: 10000000.<br>Reg office and postal address: 12 Harbour Row, London, E1 0AA, UK</p>

</main>
</body>
</html>
```